Shop front signage design for Bubble Tea Shop

Plum Harbor is Sydney based Green Tea Shop.We are looking for a modern and sleek signage for shop front end. We have Aluminium Composite Panel and Awning sign at the shop front. We will keep Aluminium composite panel simple with logo and text. We are after awning design which is above glass door and under the panel. Old Awning is PVC foam in two pieces 2310mm w x 1000mm h. We need someone to design awing. It should reflect Bubble tea and using bubble tea cups with pearls is essential. Stock images can be used. Avoid using icons or illustrative icons as we are after real images of bubble tea cup. This is to ensure that the brand is not taken as juice shop or cafe.
Panel Dimensions is 5250 mm w x 580 mm h.Awning/ Fascia sign is 4720 mm w x 1000 mm h.
Logo and signage concept is attached.

Target Market(s)

Corporate Male and Female, school, general public.

Colors
f36e22
333333
000000
eaeaea
cbcbcb

Requirements
Must have
• Bubble tea cups with fruit or milk tea.
Should not have
• Icons, illustration

```html
<!DOCTYPE html>
<html lang="en">
<head>
<meta charset="utf-8">
<title>Plum Harbor – Awning Signage</title>
<link rel="stylesheet" href="https://fonts.googleapis.com/css2?family=Nunito:wght@800&family=Lobster&family=Roboto+Condensed:wght@700&family=Montserrat:wght@600&display=swap">
<style>
  :root {
    --orange: #f36e22;
    --charcoal: #333333;
    --black: #000000;
    --light-grey: #eaeaea;
    --mid-grey: #cbcbcb;
    --white: #ffffff;
  }
  * { box-sizing: border-box; margin: 0; padding: 0; }
  html, body {
    width: 1200px;
    height: 750px;
    overflow: hidden;
    background: var(--light-grey);
  }
  .canvas {
    position: relative;
    width: 1200px;
    height: 750px;
  }
  .sign {
    position: absolute;
    left: 50px;
    width: 1100px;
    height: 234px;
    background: var(--white);
    overflow: hidden;
    box-shadow: 0 4px 10px rgba(0,0,0,0.18);
  }
  .sign--split { top: 110px; }
  .sign--banded { top: 404px; }

  .sign__shape {
    position: absolute;
    inset: 0;
  }

  .brand {
    position: absolute;
    display: flex;
    align-items: center;
    font-family: "Nunito", sans-serif;
    font-weight: 800;
    letter-spacing: -0.01em;
    white-space: nowrap;
  }
  .brand__mark {
    flex: none;
    border-radius: 50%;
  }
  .sign--split .brand {
    left: 48px;
    top: 91px;
    color: var(--white);
    font-size: 46px;
    gap: 20px;
  }
  .sign--split .brand__mark {
    width: 72px;
    height: 72px;
    border: 6px solid var(--white);
  }
  .sign--banded .brand {
    left: 38px;
    top: 83px;
    color: var(--black);
    font-size: 60px;
    gap: 24px;
  }
  .sign--banded .brand__mark {
    width: 98px;
    height: 98px;
    border: 9px solid var(--black);
  }

  .cups-photo {
    position: absolute;
    border-radius: 6px;
    background: linear-gradient(90deg,
      #e6e3f2 0%, #f4c6d6 24%, #f3ecb0 46%, #bfe6c4 68%, #efc58f 90%, #f3f0ec 100%);
  }
  .sign--split .cups-photo { left: 540px; top: 17px; width: 327px; height: 168px; }
  .sign--banded .cups-photo { left: 554px; top: 19px; width: 334px; height: 162px; }

  .tagline {
    position: absolute;
    text-align: right;
  }
  .tagline__fresh {
    display: block;
    font-family: "Lobster", cursive;
    color: var(--orange);
    line-height: 1;
  }
  .tagline__swoosh {
    display: block;
    margin-top: -6px;
  }
  .tagline__juice {
    display: block;
    font-family: Arial, "Helvetica Neue", sans-serif;
    color: var(--black);
    line-height: 1;
  }
  .sign--split .tagline { left: 900px; top: 42px; width: 172px; }
  .sign--split .tagline__fresh { font-size: 62px; }
  .sign--split .tagline__juice { font-size: 34px; margin-top: -2px; }
  .sign--banded .tagline { left: 912px; top: 54px; width: 160px; }
  .sign--banded .tagline__fresh { font-size: 56px; }
  .sign--banded .tagline__juice { font-size: 32px; margin-top: -2px; }

  .menu-line {
    position: absolute;
    left: 570px;
    top: 192px;
    width: 505px;
    display: flex;
    justify-content: space-between;
    align-items: center;
    font-family: "Roboto Condensed", sans-serif;
    font-weight: 700;
    font-size: 24px;
    color: var(--black);
  }
  .menu-line__divider {
    font-weight: 400;
    font-size: 22px;
  }

  .menu-band {
    position: absolute;
    left: 0;
    bottom: 0;
    width: 100%;
    height: 46px;
    background: var(--black);
    display: flex;
    justify-content: space-between;
    align-items: center;
    padding: 0 30px 0 164px;
    font-family: "Montserrat", sans-serif;
    font-weight: 600;
    font-size: 19px;
    letter-spacing: 0.36em;
    color: var(--white);
  }
  .menu-band__divider {
    letter-spacing: 0;
    font-weight: 400;
  }
</style>
</head>
<body>
<main class="canvas">

  <section class="sign sign--split" aria-label="Awning option one">
    <svg class="sign__shape" width="1100" height="234" viewBox="0 0 1100 234" aria-hidden="true">
      <path d="M0 0 H458 Q468 150 525 234 H0 Z" fill="var(--black)"/>
      <path d="M476 0 Q482 150 542 234" fill="none" stroke="var(--black)" stroke-width="3"/>
    </svg>

    <div class="brand">
      <span class="brand__mark"></span>
      <span class="brand__name">Plum Harbor</span>
    </div>

    <div class="cups-photo" role="img" aria-label="Photo of five bubble tea cups with domed lids, coloured straws and tapioca pearls: taro, strawberry, mango, green tea and milk tea"></div>

    <div class="tagline">
      <span class="tagline__fresh">Fresh</span>
      <svg class="tagline__swoosh" width="172" height="10" viewBox="0 0 172 10" aria-hidden="true">
        <path d="M0 9 Q90 2 172 1" fill="none" stroke="var(--orange)" stroke-width="2"/>
      </svg>
      <span class="tagline__juice">Juice</span>
    </div>

    <div class="menu-line">
      <span>Pearl Tea</span><span class="menu-line__divider">|</span>
      <span>Fruit Tea</span><span class="menu-line__divider">|</span>
      <span>Green Tea</span><span class="menu-line__divider">|</span>
      <span>Ice Frappe</span>
    </div>
  </section>

  <section class="sign sign--banded" aria-label="Awning option two">
    <div class="brand">
      <span class="brand__mark"></span>
      <span class="brand__name">Plum Harbor</span>
    </div>

    <div class="cups-photo" role="img" aria-label="Photo of five bubble tea cups with domed lids, coloured straws and tapioca pearls: taro, strawberry, mango, green tea and milk tea"></div>

    <div class="tagline">
      <span class="tagline__fresh">Fresh</span>
      <svg class="tagline__swoosh" width="160" height="10" viewBox="0 0 160 10" aria-hidden="true">
        <path d="M0 9 Q85 2 160 1" fill="none" stroke="var(--orange)" stroke-width="2"/>
      </svg>
      <span class="tagline__juice">Juice</span>
    </div>

    <div class="menu-band">
      <span>PEARL TEA</span><span class="menu-band__divider">|</span>
      <span>FRUIT TEA</span><span class="menu-band__divider">|</span>
      <span>GREEN TEA</span><span class="menu-band__divider">|</span>
      <span>ICE FRAPPE</span>
    </div>
  </section>

</main>
</body>
</html>
```